Need Eye Catching For Sale By Owner Signs

In need of a Eye Catching For Sale By Owner Sign design. I plan on using the sign to market buildings and raw land that I own. The design should be able to scale to different rectangular dimensions for example a yard stake sign or a large 4' x 6' sign to be tacked to plywood. The design should have a dead space near the bottom that I can insert more detail information into at a later time.

The main tag line "For Sale By Owner" and the contact number "319-562-4097" needs to be easily be read from a distance.

```html
<!DOCTYPE html>
<html lang="en">
<head>
<meta charset="utf-8">
<title>For Sale By Owner Sign</title>
<link rel="stylesheet" href="https://fonts.googleapis.com/css2?family=Jost:wght@600&display=swap">
<style>
  :root {
    --sign-white: #ffffff;
    --sign-blue: #3a89c9;
    --sign-pale-blue: #9cc4e4;
    --sign-charcoal: #58595b;
  }
  html, body {
    margin: 0;
    padding: 0;
    width: 1200px;
    height: 800px;
    overflow: hidden;
    background: var(--sign-white);
  }
  .sign {
    display: block;
    width: 1200px;
    height: 800px;
  }
  .sign__headline,
  .sign__subline,
  .sign__phone {
    font-family: "Jost", "Futura", sans-serif;
    font-weight: 600;
  }
  .sign__headline { fill: var(--sign-charcoal); font-size: 224px; }
  .sign__subline { fill: var(--sign-blue); font-size: 124px; }
  .sign__phone { fill: var(--sign-white); font-size: 128px; }
  .sign__panel { fill: var(--sign-blue); }
  .sign__arrow-area { fill: url(#arrowTone); }
</style>
</head>
<body>
<svg class="sign" viewBox="0 0 1200 800" xmlns="http://www.w3.org/2000/svg" aria-label="For Sale By Owner sign">
  <defs>
    <linearGradient id="arrowTone" x1="0" y1="0" x2="0" y2="1">
      <stop offset="0" stop-color="var(--sign-pale-blue)"/>
      <stop offset="0.5" stop-color="var(--sign-pale-blue)"/>
      <stop offset="1" stop-color="var(--sign-blue)"/>
    </linearGradient>
  </defs>

  <rect class="sign__panel" x="0" y="400" width="1200" height="400"/>

  <rect class="sign__arrow-area" x="0" y="280" width="390" height="240"
        role="img" aria-label="Striped chevron arrows pointing left"/>

  <text class="sign__headline" x="78" y="252" textLength="1044" lengthAdjust="spacingAndGlyphs">FOR SALE</text>
  <text class="sign__subline" x="470" y="365" textLength="648" lengthAdjust="spacingAndGlyphs">BY OWNER</text>

  <text class="sign__phone" x="600" y="700" text-anchor="middle">319-562-4097</text>
</svg>
</body>
</html>
```